New Business Card Design Project

Make a kick ass business card for The Otter Tea Mug, using the designs. I also might like the 2nd place design logo on the back? Maybe all black with that? Not sure. Also, I'm cool with it being on metal, plastic, glass? or whatever for the business card. Maybe shaped like a shark? Let me know what else you need? Would like designs in the next day or so. Thank you.
Target Market(s)
Anyone that is cool
Contact Information for Business Card
Name: Dorian Fenwick
Phone: 317.594.8126
inventor/creator/entrepreneur/owner
www.theottertyeamug.example
social media links
https://www.facebook.com/theottertyeamug
https://twitter.com/otter_brew
https://www.instagram.com/theottertyeamug/
I'll get the Pinterest one soon
Colors
Designer to choose colors to be used in the design.
Requirements
Must have
- The Otter Tea Mug
- www.theottertyeamug.example
- social media tags?
- My logos and picture/photo of wine glass
Nice to have
- Maybe shaped like a wine glass or shark
- I'll let you decide but my same colors from my website would be nice

```html
<!DOCTYPE html>
<html lang="en">
<head>
<meta charset="utf-8">
<title>Otter Tea Mug — Business Card</title>
<link rel="stylesheet" href="https://fonts.googleapis.com/css2?family=Lato:wght@400;700&family=Mulish:wght@300;400&display=swap">
<style>
  :root {
    --backdrop: #5e5e5e;
    --card-red: #bd444c;
    --card-black: #0c0c0c;
    --ink-light: #d9d9d9;
    --rule: #d7a3a6;
    --pattern-top: #1c1c1c;
  }
  * { margin: 0; padding: 0; box-sizing: border-box; }
  html, body { width: 1200px; height: 960px; overflow: hidden; background: var(--backdrop); }
  .stage { position: relative; width: 1200px; height: 960px; }
  .card {
    position: absolute; top: 176px; width: 364px; height: 638px;
    border-radius: 22px; overflow: hidden;
  }
  .card--front { left: 168px; background: var(--card-red); color: var(--ink-light); font-family: "Lato", sans-serif; text-align: center; }
  .card--back { left: 662px; background: var(--card-black); color: var(--ink-light); font-family: "Mulish", sans-serif; text-align: center; }

  .brand-mark { position: absolute; left: 0; right: 0; top: 70px; }
  .brand-mark__dot { width: 92px; height: 92px; border-radius: 50%; background: var(--ink-light); margin: 0 auto; }
  .brand-mark__name { margin-top: 26px; font-size: 24px; font-weight: 700; letter-spacing: 0.5px; }

  .holder-name { position: absolute; left: 0; right: 0; top: 333px; font-size: 27px; font-weight: 700; letter-spacing: 0.3px; }
  .holder-role { position: absolute; left: 0; right: 0; top: 372px; font-size: 17px; font-weight: 400; }

  .divider { position: absolute; left: 70px; width: 224px; height: 14px; }
  .divider::before { content: ""; position: absolute; left: 0; right: 0; top: 50%; border-top: 1px solid var(--rule); }
  .divider__icons { position: relative; display: flex; justify-content: center; gap: 3px; }
  .divider__icons span, .divider__icons svg { background: var(--card-red); }
  .divider--contact { top: 406px; height: 20px; }
  .divider--social { top: 499px; }
  .icon-ring { display: block; width: 20px; height: 20px; border: 1.3px solid var(--ink-light); border-radius: 50%; }
  .icon-dot { display: block; width: 14px; height: 14px; border: 1.2px solid var(--ink-light); border-radius: 50%; }

  .contact-line { position: absolute; left: 0; right: 0; font-size: 15px; }
  .contact-line--phone { top: 440px; }
  .contact-line--web { top: 467px; }
  .social-list { position: absolute; left: 0; right: 0; top: 526px; list-style: none; font-size: 15px; line-height: 20px; }

  .back-pattern {
    position: absolute; left: 0; right: 0; top: 0; height: 470px;
    background: linear-gradient(to bottom, var(--pattern-top), var(--card-black));
  }
  .back-wordmark { position: absolute; left: 0; right: 0; top: 525px; font-size: 35px; font-weight: 300; letter-spacing: 0.2px; }
  .back-tagline { position: absolute; left: 0; right: 0; top: 576px; font-size: 14px; font-weight: 400; color: #b9b9b9; }
</style>
</head>
<body>
<main class="stage">
  <section class="card card--front" aria-label="Card front">
    <div class="brand-mark">
      <div class="brand-mark__dot"></div>
      <div class="brand-mark__name">Otter Tea Mug</div>
    </div>
    <h1 class="holder-name">DORIAN FENWICK</h1>
    <p class="holder-role">Inventor</p>

    <div class="divider divider--contact">
      <div class="divider__icons">
        <svg class="icon-ring" viewBox="0 0 20 20" aria-label="Phone" role="img">
          <path d="M7 5.5l1.6 2.4-1 1c.7 1.4 1.8 2.5 3.2 3.2l1-1 2.4 1.6-.9 1.6c-3.8-.3-6.9-3.4-7.2-7.2z" fill="none" stroke="#d9d9d9" stroke-width="1.1" stroke-linejoin="round"/>
        </svg>
        <svg class="icon-ring" viewBox="0 0 20 20" aria-label="Website" role="img">
          <g fill="none" stroke="#d9d9d9" stroke-width="1">
            <circle cx="9.5" cy="9.5" r="5"/>
            <ellipse cx="9.5" cy="9.5" rx="2.2" ry="5"/>
            <path d="M4.5 9.5h10M5.3 7h8.4M5.3 12h8.4"/>
          </g>
        </svg>
      </div>
    </div>
    <p class="contact-line contact-line--phone">317.594.8126</p>
    <p class="contact-line contact-line--web">www.theottertyeamug.example</p>

    <div class="divider divider--social">
      <div class="divider__icons">
        <span class="icon-dot"></span><span class="icon-dot"></span><span class="icon-dot"></span><span class="icon-dot"></span>
      </div>
    </div>
    <ul class="social-list">
      <li>facebook.com/theottertyeamug</li>
      <li>twitter.com/otter_brew</li>
      <li>instagram.com/theottertyeamug/</li>
      <li>pinterest.com/theottertyeamug/</li>
    </ul>
  </section>

  <section class="card card--back" aria-label="Card back">
    <div class="back-pattern" role="img" aria-label="Faint repeating pattern of brand glasses"></div>
    <p class="back-wordmark">OtterTeaMug</p>
    <p class="back-tagline">inventor | creator | entrepreneur | owner</p>
  </section>
</main>
</body>
</html>
```